Innovative Bitcoin Powerpoint Presentation

I have constructred most of the data for a 15 page powerpoint presentation on an innovative bitcoin idea that provides access to fiat currency with bitcoin hodlings

I need this to look great as a first blush to potential investors

Reason: updated deck and name

Target Market(s)

Venture Capital firms and private equity firms

Requirements
Must have
• Fun, innovateive deck, very clean
Should not have
• any generic feel - no templates

```html
<!DOCTYPE html>
<html lang="en">
<head>
<meta charset="UTF-8">
<title>Project Title Here</title>
<link rel="stylesheet" href="https://fonts.googleapis.com/css2?family=Roboto+Condensed:wght@400&family=Roboto:wght@300&display=swap">
<style>
  :root {
    --header-deep: #0d3f7a;
    --header-mid: #1a65b0;
    --header-light: #2f86cf;
    --white: #ffffff;
    --metric-blue: #3574b7;
    --metric-orange: #fca64b;
    --metric-teal: #36b9a3;
    --connector: #8f8f8f;
    --label-text: #555555;
    --footer-orange: #fe9300;
  }
  html, body {
    margin: 0;
    padding: 0;
    width: 1200px;
    height: 900px;
    overflow: hidden;
    background: var(--white);
  }
  .slide {
    position: relative;
    width: 1200px;
    height: 900px;
    background: var(--white);
    font-family: "Roboto Condensed", "Arial Narrow", sans-serif;
  }
  .slide-header {
    position: absolute;
    left: 0; top: 0;
    width: 1200px; height: 128px;
  }
  .header-art {
    position: absolute;
    inset: 0;
    background: linear-gradient(100deg, var(--header-deep) 0%, var(--header-mid) 55%, var(--header-light) 100%);
  }
  .slide-title {
    position: absolute;
    left: 48px; top: 34px;
    margin: 0;
    font-weight: 400;
    font-size: 60px;
    line-height: 1;
    color: var(--white);
    letter-spacing: -0.5px;
  }
  .brand {
    position: absolute;
    right: 24px; top: 46px;
    display: flex;
    align-items: center;
    gap: 10px;
    color: var(--white);
    font-size: 32px;
    line-height: 1;
  }
  .brand-dot {
    width: 22px; height: 22px;
    border-radius: 50%;
    background: var(--white);
  }
  .metric {
    position: absolute;
    top: 317px;
    width: 261px;
  }
  .metric--one { left: 93px; --accent: var(--metric-blue); }
  .metric--two { left: 484px; --accent: var(--metric-orange); }
  .metric--three { left: 875px; --accent: var(--metric-teal); }
  .metric-value {
    height: 131px;
    border-radius: 4px;
    background: var(--accent);
    box-shadow: 0 0 0 5px var(--white), 0 0 9px 5px rgba(0,0,0,0.12);
    display: flex;
    align-items: center;
    justify-content: center;
    font-family: "Roboto", "Arial", sans-serif;
    font-weight: 300;
    font-size: 70px;
    color: var(--white);
  }
  .metric-connector {
    width: 3px;
    height: 89px;
    margin: 0 auto;
    background: var(--connector);
  }
  .metric-label {
    box-sizing: border-box;
    width: 258px;
    height: 128px;
    margin: 5px auto 0;
    border: 1.5px solid var(--accent);
    border-radius: 4px;
    display: flex;
    align-items: center;
    justify-content: center;
    text-align: center;
    font-size: 34px;
    line-height: 44px;
    color: var(--label-text);
    text-transform: uppercase;
  }
  .footer-rule {
    position: absolute;
    left: 0; top: 843px;
    width: 1200px; height: 3px;
    background: var(--footer-orange);
  }
  .slide-footer {
    position: absolute;
    left: 0; top: 852px;
    width: 1200px; height: 48px;
    background: var(--footer-orange);
  }
  .copyright {
    position: absolute;
    left: 13px; top: 12px;
    margin: 0;
    font-size: 23px;
    line-height: 1;
    color: var(--white);
  }
</style>
</head>
<body>
  <main class="slide">
    <header class="slide-header">
      <div class="header-art" role="img" aria-label="Blue technology background with binary digits and circuit lines"></div>
      <h1 class="slide-title">Project Title Here</h1>
      <div class="brand"><span class="brand-dot"></span><span>Coinvale</span></div>
    </header>

    <section class="metric metric--one">
      <div class="metric-value">13.5m</div>
      <div class="metric-connector"></div>
      <div class="metric-label">BTC in<br>circulation</div>
    </section>
    <section class="metric metric--two">
      <div class="metric-value">13.5m</div>
      <div class="metric-connector"></div>
      <div class="metric-label">BTC in<br>circulation</div>
    </section>
    <section class="metric metric--three">
      <div class="metric-value">13.5m</div>
      <div class="metric-connector"></div>
      <div class="metric-label">BTC in<br>circulation</div>
    </section>

    <div class="footer-rule"></div>
    <footer class="slide-footer">
      <p class="copyright">Copyright text here</p>
    </footer>
  </main>
</body>
</html>
```